author needs a Book Cover design

Needs a book cover design that matches the title in some way.
Book Title is- 9 Lanterns Beneath a Quiet Harbor Tonight.
Subtile- Harvest Lessons Across Ordinary Seasons.
Author Name:-Desmond Okorefe, Jr.

Final Design is subject to Book Publisher's requirement.

Font styles to use
Serif

Requirements
Must have
• Follow these recommended specifications for your cover file:
• Page Size: Your cover should be a single (one-piece) PDF that includes the back cover, spine, and front cover. You can submit your cover on any size page as long as the printable area is measured exactly for your book's trim size, spine width, and allows at least .125” bleed, centered horizontally and vertically.
• Minimum Cover Width: Bleed + Back Cover Trim Size + Spine Width + Front Cover Trim Size + Bleed
• Minimum Cover Height: Bleed + Book Height Trim Size + Bleed
• Trim Size: Your cover should be the same trim size as you choose in the Title Information when setting up your book. For example, submitting a cover that was previously used for a 6.25” x 9.25” book would not work for a 6” x 9” book.
• Barcodes: For manufacturing and distribution reasons, your book's back cover must include a valid ISBN barcode. If your cover already has an ISBN barcode, make sure it is high-resolution, or at least 300 dpi, and 1.5" - 2" in width with proportional height. Ideally, this barcode should be 2” wide by 1.2” tall. Also, check to make sure you have the rights to use the ISBN on your cover, because not all services allow you to use their ISBNs elsewhere.
• QR codes: There are no set size restrictions, but the quality (resolution) of the image must be set to at least 300 dpi. Make sure you have the rights to use the code.
• If your artwork does not include a barcode, we will automatically add one in the lower right-hand corner of your book's back cover, free of charge. Our system will place the ISBN barcode in a space 2" wide and 1.2" tall. The bottom of this barcode is located 1/4" up from the bottom trim line of the cover. The right side of the barcode is located 1/4" to the left of the spine. Please ensure that you don't have any important images or text in the barcode location. You can also refer to our Artwork Templates for the exact size and position of the ISBN barcode on your final cover.
• If you don’t have an ISBN already on your cover, but you have live graphic or text elements in the location that our system will place the ISBN, you will need to move those elements or place the ISBN in a different location yourself.
• Publishing Logos: We do not add our logo to your book.
• Spine Width and Variance: If your artwork was created for a different service, please make sure that the spine width of your current cover matches our spine width. Different services may use different paper thickness, which is why the spine width of your cover artwork could be correct for another service but incorrect for our service.
• Ideally, you should avoid hard vertical lines separating your front or back cover panels from your spine and should allow for at least a .125" variance of your spine on each side (for example, the text on a 1" spine should be no larger than .75" wide). For books with a page count of less than 130 pages, we strongly recommend a blank spine.
• Your spine width should be calculated based on the number of pages in your book and using the appropriate formula:
• Black and White Interior Book Spine Width:
• White paper: Number of pages x .002252 = Spine width in inches
• Cream paper: Number of pages x .0025 = Spine width in inches
• Color Interior Book Spine Width:
• Number of pages x .002347 = Spine width in inches
• Example of spine width calculation for a 120-page black and white interior book with white paper:
• 120 x .002252 = .27" spine width
• Text and Image Placement: All live cover elements, or text and images that cannot be cut, must be at least .125" inside the trim lines to ensure no important elements are cut during the bookmaking process and the appearance of your printed books is consistent.
• Bleed: Your cover's background must extend at least .125" beyond the final trim line to accommodate for cutting/trimming tolerance.
• Crop/Registration Marks: Please do not include any crop or registration marks on your files, as they may interfere with the binding process or appear on the cover. We use our own measurements, specific to our systems, for cutting and binding; crop or registration marks placed by you could interfere with this process.
• Images and Fonts: Any images you include on your book's cover may be tagged with your choice of CMYK or RGB profiles or left untagged in a generic color space. All images should be sized at 100%, flattened to one layer and placed in your native document at a resolution of at least 300 DPI. You should also embed all fonts in your PDF file.
• Desmond, I hope this information is helpful to you. Please feel free to contact us if you have any other questions or concerns.
• Best regards,
• *WILL SUPPLY THE PAGE NUMBERS INFORMATION
• Lisbeth
• PrintHollow Member Services
Nice to have
• An attractive design that matches the title. Design can include backgrounds

```html
<!DOCTYPE html>
<html lang="en">
<head>
<meta charset="utf-8">
<title>9 Lanterns Beneath a Quiet Harbor Tonight — Book Cover</title>
<link rel="stylesheet" href="https://fonts.googleapis.com/css2?family=Cinzel:wght@400&family=Cinzel+Decorative:wght@400&display=swap">
<style>
  :root {
    --stage: #e4e4e4;
    --cover-top: #c9c8c2;
    --cover-light: #e2e1dc;
    --cover-mid: #d3d2cc;
    --cover-low: #7c7b77;
    --ink: #1d1d1d;
    --title-red: #d9252b;
    --shade-dark: #6d6c69;
    --shade-soft: #9e9d99;
  }
  * { margin: 0; padding: 0; box-sizing: border-box; }
  html, body {
    width: 1200px;
    height: 1099px;
    overflow: hidden;
    background: var(--stage);
  }
  .stage {
    width: 1200px;
    height: 1099px;
    display: flex;
    align-items: center;
    justify-content: center;
  }
  .cover {
    position: relative;
    width: 610px;
    height: 960px;
    overflow: hidden;
    background:
      radial-gradient(ellipse 70% 40% at 60% 38%, var(--cover-light) 0%, rgba(226,225,220,0) 100%),
      linear-gradient(180deg, var(--cover-top) 0%, var(--cover-mid) 40%, var(--cover-low) 100%);
  }
  .cover-art {
    position: absolute;
    left: 0;
    right: 0;
    top: 520px;
    bottom: 0;
    background:
      radial-gradient(ellipse 34% 48% at 30% 62%, var(--shade-dark) 0%, rgba(109,108,105,0) 80%),
      radial-gradient(ellipse 40% 55% at 76% 48%, var(--shade-soft) 0%, rgba(158,157,153,0) 85%),
      linear-gradient(180deg, rgba(211,210,204,0) 0%, var(--shade-dark) 100%);
  }
  .author {
    position: absolute;
    top: 22px;
    left: 0;
    right: 0;
    text-align: center;
    font-family: "Cinzel", serif;
    font-size: 36px;
    color: var(--ink);
  }
  .title {
    font-family: "Cinzel Decorative", serif;
    font-weight: 400;
    color: var(--title-red);
  }
  .title-numeral {
    position: absolute;
    left: 34px;
    top: 84px;
    font-family: "Cinzel", serif;
    font-size: 262px;
    line-height: 1;
  }
  .title-line {
    position: absolute;
    right: 62px;
    line-height: 1;
    white-space: nowrap;
  }
  .title-line--one   { top: 140px; font-size: 80px; }
  .title-line--two   { top: 235px; font-size: 68px; right: 50px; }
  .title-line--three { top: 323px; font-size: 58px; }
  .title-line--four  { top: 406px; font-size: 64px; }
  .subtitle {
    position: absolute;
    top: 476px;
    left: 0;
    right: 0;
    padding-right: 24px;
    text-align: center;
    font-family: "Cinzel", serif;
    font-size: 34px;
    line-height: 45px;
    color: var(--ink);
  }
</style>
</head>
<body>
  <main class="stage">
    <section class="cover">
      <div class="cover-art" role="img" aria-label="Soft-focus photograph of shadowy silhouettes cast on a pale wall"></div>
      <p class="author">Desmond Okorefe, Jr.</p>
      <h1 class="title">
        <span class="title-numeral">9</span>
        <span class="title-line title-line--one">Lanterns</span>
        <span class="title-line title-line--two">Beneath a</span>
        <span class="title-line title-line--three">Quiet Harbor</span>
        <span class="title-line title-line--four">Tonight</span>
      </h1>
      <p class="subtitle">Harvest Lessons<br>Across Ordinary Seasons</p>
    </section>
  </main>
</body>
</html>
```